Corporate Web Design

Hello Designers,
Thank you for wanting to participate in designing a web design.
First off let me introduce ourselves, we are a precious metals refinery that is base in the west coast. Our Name is Sterling Harbor Metals Refinery. Our sole goal for this website is simplicity yet cleanliness and elegance. We want to demonstrate the process and procedures of what we do and who we are.
The Lay out:
We want about 4-5 Tabs that will help guide our customers through our website with ease. Some ideas of what we want to call the tabs might be….
1. Home
- This tab will take them to the home page
2. Contact Us
- Our contact information
- Client contact form
- Some sort of membership form?
3. Pick-up Service
- This tab will explain how this process works and what it in tells.
- This page will also have a section for requirements.
- This pickup service will only be available for members and people that have a good account with us.
4. How it Works
- This page will explain who we are and how we work.
- I would like to somehow creatively show the process and the steps we take in melting their gold.
Effects:
An effect that I would want to see is a live precious metal stock price. This price will automatically update and post the most recent and current price on the market of what the gold, silver etc prices. Here is a link of a company that has something similar, http://qlvt-refining.example/ what I like about this spot price pop up, is that it follows them all over the page. I like that idea.
I would also like some sort of slide show that has videos and demonstrations of our company and business.
These are all Websites of our competitors that we like many ideas from.
http://www.bzkw.example/
What we like about this website is the tab that says “Request Pick-up” With a form that they have to fill out. We would want more than just a form; we would want some sort of membership application.
http://vexmetals.example/
What I like about this website is the slideshow. It’s very simple yet professional. This is something that I would like to incorporate into our website. I also like the live metal market price.
http://qlvt-refining.example/
This is another example of a website that has a live spot price of the gold market. I like how the gold price follows you around the page. I would like to see some of your ideas with this.
http://www.dunmetals.example/
This website is very clean and simple. I like the colors. I would like a little more character than what they have but I like the simplicity.
The colors we like are black, white, silver, gold, Royal Blue etc; basically anything that creates a clean atmosphere. These colors match our logo and also have a very elegant and professional perception to them. Please do not limit yourselves to only our suggestions
These are links to our Logo with all different colors.
https://files.example/s/k27m4p91rtz8vqa/LOGO_black_background.png
https://files.example/s/9wnb3x61hdq2lfe/LOGO_black.png
https://files.example/s/m8rc215jqpv4kzo/LOGO_transparent_background.png
https://files.example/s/t3fy804lwmn6bsu/LOGO_white_background.png
These are links to a brochure of our business that represents and shows the process of what we do and demonstrates who we are.
https://files.example/s/h6dv592kqcx1rwa/inside_1.pdf
https://files.example/s/p4gl736nybe9tcu/inside_2.pdf
Bottom line we want to see examples of ideas and layouts that you have for a website. Please upload them and We will comment back on them.

```html
<!DOCTYPE html>
<html lang="en">
<head>
<meta charset="utf-8">
<title>Sterling Harbor Metals Refinery – Web Design</title>
<link rel="stylesheet" href="https://fonts.googleapis.com/css2?family=PT+Sans:wght@400;700&family=PT+Sans+Narrow:wght@400;700&family=Encode+Sans+Condensed:wght@300;400&display=swap">
<style>
:root{
  --ink:#2b3a42;
  --text:#222;
  --muted:#8a8a8a;
  --gold:#f2c400;
  --amber:#f7a800;
  --royal:#1d3a86;
  --blue:#1f3fd8;
  --sky:#16b7ee;
  --grey:#a9a9a9;
  --orange:#fb8a08;
  --paper:#fff;
}
*{margin:0;padding:0;box-sizing:border-box}
html,body{width:1200px;height:1000px;overflow:hidden;background:var(--paper)}
body{position:relative;font-family:"PT Sans",sans-serif;color:var(--text)}
.page{position:absolute;background:var(--paper);box-shadow:0 0 3px rgba(0,0,0,.12)}
.page--home{left:81px;top:189px;width:467px;height:574px}
.page--process{left:619px;top:189px;width:468px;height:661px}
.abs{position:absolute}

/* ticker */
.ticker{left:0;top:0;width:467px;height:29px;background:var(--ink);color:#fff;display:flex;font-size:6px}
.ticker__metal{width:61px;background:var(--amber);text-align:center;padding-top:5px;font-size:5px}
.ticker__select{display:inline-block;margin-top:2px;background:#d9d9d9;color:#555;border-radius:6px;padding:1px 8px;font-size:6px;font-weight:700}
.ticker__cell{text-align:center;padding-top:4px}
.ticker__cell b{display:block;font-size:7.5px;margin-top:3px}
.ticker__sep{border-left:1px dotted #9aa;margin:5px 0}
.handle{width:44px;height:11px;background:var(--ink);border-radius:0 0 4px 4px;display:flex;align-items:center;justify-content:center}
.handle svg{display:block}

/* brand */
.brand{text-align:right;font-family:"PT Sans",sans-serif;color:#8b6a2b;font-size:9px;letter-spacing:.6px;line-height:1}
.brand small{display:block;font-size:4px;letter-spacing:.3px;margin-top:2px}

/* nav */
.nav{display:flex;font-size:7px}
.nav__item{width:86px;text-align:center;text-transform:uppercase;position:relative}
.nav__item svg{display:block;margin:0 auto 4px}
.nav__item small{display:block;text-transform:none;font-size:5px;color:var(--muted);margin-top:1px}
.nav__item--active::after{content:"";position:absolute;left:21px;right:21px;bottom:-7px;height:3px;background:var(--blue)}

/* hero */
.hero{left:0;top:109px;width:467px;height:192px;background:linear-gradient(90deg,#c9ccd6 0%,#9aa3c4 20%,#4b5a9a 45%,#b58a6a 70%,#d8b59a 85%,#8a6a55 100%)}
.hero__panel{left:61px;top:0;width:210px;height:192px;background:rgba(30,45,120,.55)}
.hero__title{left:72px;top:38px;font-family:"PT Sans Narrow",sans-serif;color:var(--gold);font-size:28px;line-height:26px}
.hero__sub{left:72px;top:100px;font-family:"PT Sans Narrow",sans-serif;color:#fff;font-size:17px}
.hero__arrow{top:100px;width:0;height:0;border-top:8px solid transparent;border-bottom:8px solid transparent}
.hero__dots{left:213px;top:174px;display:flex;gap:9px}
.hero__dots i{width:7px;height:7px;border-radius:50%;background:rgba(0,0,0,.35);display:block}
.hero__dots i:first-child{background:var(--gold)}

/* values */
.values{left:36px;top:337px;display:flex;gap:18px}
.value{width:60px;text-align:center;font-size:7.5px;line-height:9px}
.value__disc{width:60px;height:60px;border-radius:50%;display:flex;align-items:center;justify-content:center;margin-bottom:10px}

/* bullion */
.bullion{top:470px;height:61px;width:234px}
.bullion__label{position:absolute;right:14px;top:9px;font-family:"PT Sans Narrow",sans-serif;font-size:24px;line-height:21px;text-align:right}
.bullion__label span{display:block;font-size:17px;color:#555}

/* footer */
.footer{left:0;bottom:0;width:100%;height:43px;background:var(--ink);color:#fff;font-size:5px;font-weight:700}
.footer__social{position:absolute;left:19px;top:20px;display:flex;gap:4px}
.footer__social i{width:10px;height:10px;background:#8a97a0;display:block}
.footer__copy{position:absolute;left:0;right:0;top:24px;text-align:center;padding-left:10px}

/* process page */
.process__title{left:44px;top:129px;font-family:"Encode Sans Condensed",sans-serif;font-weight:300;font-size:31px;color:#333}
.process__intro{left:42px;top:169px;width:393px;font-size:7px;line-height:8.6px;text-align:justify}
.steps{left:36px;top:226px;display:flex;gap:27px}
.steps__item{width:76px;height:76px;border-radius:50%;color:#fff;font-family:"PT Sans Narrow",sans-serif;font-size:11px;display:flex;align-items:center;padding-left:6px}
.feature{left:30px;top:322px;width:407px;height:258px;display:flex}
.feature__photo{width:262px;height:258px;background:linear-gradient(135deg,#8a7a62 0%,#c9a24a 50%,#6f5a3a 100%)}
.feature__text{width:145px;background:var(--orange);color:#fff;padding:30px 14px 0}
.feature__text h2{font-family:"Encode Sans Condensed",sans-serif;font-weight:300;font-size:38px;line-height:1;margin-bottom:14px}
.feature__text p{font-size:7px;line-height:9.3px;text-align:justify}
</style>
</head>
<body>

<!-- Home page -->
<section class="page page--home">
  <div class="abs ticker">
    <div class="ticker__metal">Real-time Price<br><span class="ticker__select">Gold ▾</span></div>
    <div class="ticker__cell" style="width:100px">LastUpdate<b>Fri May 31, 4:21 AM CDT</b></div>
    <div class="ticker__cell" style="width:40px">Bid<b>1,413.02</b></div>
    <div class="ticker__cell" style="width:38px">Ask<b>1,413.24</b></div>
    <div class="ticker__sep"></div>
    <div class="ticker__cell" style="width:44px">Low<b>1,411.86</b></div>
    <div class="ticker__cell" style="width:38px">High<b>1,421.86</b></div>
    <div class="ticker__sep"></div>
    <div class="ticker__cell" style="width:75px">Change<b>-0.49(-0.03%)</b></div>
    <div class="ticker__sep"></div>
    <div class="ticker__cell" style="width:40px"><b style="font-size:5.5px;margin:0">REFRESH</b>
      <svg width="12" height="12" viewBox="0 0 12 12" style="margin-top:3px"><g stroke="#fff" stroke-width="1.2"><path d="M6 1v2.5M6 8.5V11M1 6h2.5M8.5 6H11M2.5 2.5l1.7 1.7M7.8 7.8l1.7 1.7M2.5 9.5l1.7-1.7M7.8 4.2l1.7-1.7"/></g></svg>
    </div>
  </div>
  <div class="abs handle" style="left:215px;top:29px"><svg width="12" height="6"><path d="M0 1h12M0 3h12M0 5h12" stroke="#fff" stroke-width="1"/></svg></div>
  <div class="abs brand" style="right:8px;top:34px">STERLING HARBOR<small>precious metals refinery</small></div>

  <nav class="abs nav" style="left:40px;top:66px">
    <div class="nav__item nav__item--active"><svg width="14" height="12" viewBox="0 0 14 12"><path d="M7 0L0 6h2v6h4V8h2v4h4V6h2z" fill="#111"/></svg>Home<small>welcome</small></div>
    <div class="nav__item"><svg width="12" height="12" viewBox="0 0 12 12"><rect x=".5" y=".5" width="11" height="11" fill="none" stroke="#111" stroke-dasharray="1.5 1"/><path d="M6 3v6M3.5 5.5L6 3l2.5 2.5" stroke="#111" fill="none"/></svg>Pick-up Service<small>section requirements</small></div>
    <div class="nav__item"><svg width="14" height="12" viewBox="0 0 14 12"><circle cx="5" cy="5" r="3" fill="none" stroke="#111" stroke-width="2" stroke-dasharray="1.5 .8"/><circle cx="10.5" cy="9" r="2" fill="none" stroke="#111" stroke-width="1.6"/></svg>How it Works<small>flow &amp; process</small></div>
    <div class="nav__item"><svg width="13" height="10" viewBox="0 0 13 10"><rect x=".6" y=".6" width="11.8" height="8.8" fill="none" stroke="#111" stroke-width="1.2"/><path d="M.6.6l5.9 5 5.9-5" fill="none" stroke="#111" stroke-width="1.2"/></svg>Contact Us<small>keep in touch</small></div>
  </nav>

  <div class="abs hero" role="img" aria-label="Photo of a refinery worker in protective gear pouring molten metal">
    <div class="abs hero__panel"></div>
    <div class="abs hero__title">We are a precious<br>metals refinery</div>
    <div class="abs hero__sub">that is base in the west coast.</div>
    <div class="abs hero__arrow" style="left:20px;border-right:12px solid rgba(255,255,255,.7)"></div>
    <div class="abs hero__arrow" style="left:436px;border-left:12px solid rgba(255,255,255,.7)"></div>
    <div class="abs hero__dots"><i></i><i></i><i></i><i></i></div>
  </div>

  <div class="abs values">
    <div class="value"><div class="value__disc" style="background:var(--grey)"><svg width="30" height="24" viewBox="0 0 30 24" fill="#fff"><circle cx="15" cy="5" r="4"/><rect x="10" y="10" width="10" height="13" rx="3"/><circle cx="6" cy="7" r="3"/><rect x="2" y="11" width="8" height="10" rx="2"/><circle cx="24" cy="7" r="3"/><rect x="20" y="11" width="8" height="10" rx="2"/></svg></div>Transparency</div>
    <div class="value"><div class="value__disc" style="background:var(--royal)"><svg width="28" height="28" viewBox="0 0 28 28"><circle cx="13" cy="15" r="11" fill="#fff"/><circle cx="13" cy="15" r="7" fill="var(--royal)"/><circle cx="13" cy="15" r="3.5" fill="#fff"/><path d="M13 15L25 3" stroke="#fff" stroke-width="2"/></svg></div>Accuracy</div>
    <div class="value"><div class="value__disc" style="background:var(--sky)"><svg width="30" height="28" viewBox="0 0 30 28"><path d="M3 22A12 12 0 1 1 27 22z" fill="none" stroke="#fff" stroke-width="2.5"/><path d="M15 20L21 10" stroke="#fff" stroke-width="2.5"/><circle cx="15" cy="20" r="2.5" fill="#fff"/></svg></div>One Day<br>Settlements</div>
    <div class="value"><div class="value__disc" style="background:var(--blue)"><svg width="30" height="28" viewBox="0 0 30 28" fill="#fff"><circle cx="12" cy="7" r="6"/><path d="M1 27c0-8 5-12 11-12s8 2 9 4v8z"/><circle cx="23" cy="21" r="6" stroke="var(--blue)" stroke-width="1.5"/><text x="23" y="24.5" font-size="9" font-family="PT Sans" font-weight="700" fill="var(--blue)" text-anchor="middle">$</text></svg></div>Cash<br>Payment</div>
    <div class="value"><div class="value__disc" style="background:var(--royal)"><svg width="28" height="24" viewBox="0 0 28 24"><rect x="1" y="2" width="26" height="18" fill="none" stroke="#fff" stroke-width="2"/><circle cx="8" cy="10" r="3.5" fill="#fff"/><path d="M6 13l-1 7 3-2 3 2-1-7" fill="#fff"/><path d="M14 8h9M14 12h9M14 16h6" stroke="#fff" stroke-width="1.5"/></svg></div>Trust</div>
  </div>

  <div class="abs bullion" style="left:0;background:linear-gradient(90deg,#c9a25a,#e8cfa6 60%,#efdcbf)" role="img" aria-label="Gold coins and bullion bars">
    <div class="bullion__label" style="color:var(--gold)">GOLD<span>BULLION</span></div>
  </div>
  <div class="abs bullion" style="left:234px;width:233px;background:linear-gradient(90deg,#8f939c,#c8c8c8 45%,#a9a7a2)" role="img" aria-label="Silver coins and bullion bars">
    <div class="bullion__label" style="color:#fff">SILVER<span style="color:#fff">BULLION</span></div>
  </div>

  <footer class="abs footer">
    <div class="footer__social"><i></i><i></i><i></i></div>
    <div class="footer__copy">COPYRIGHT , ALL RIGHT RESERVED 2013 | TERMS &amp; CONDITIONS APPLY</div>
  </footer>
</section>

<!-- How it works page -->
<section class="page page--process">
  <div class="abs handle" style="left:216px;top:0"><svg width="12" height="6"><path d="M0 1h12M0 3h12M0 5h12" stroke="#fff" stroke-width="1"/></svg></div>
  <div class="abs brand" style="right:8px;top:34px">STERLING HARBOR<small>precious metals refinery</small></div>

  <nav class="abs nav" style="left:41px;top:65px">
    <div class="nav__item"><svg width="14" height="12" viewBox="0 0 14 12"><path d="M7 0L0 6h2v6h4V8h2v4h4V6h2z" fill="#111"/></svg>Home<small>welcome</small></div>
    <div class="nav__item"><svg width="12" height="12" viewBox="0 0 12 12"><rect x=".5" y=".5" width="11" height="11" fill="none" stroke="#111" stroke-dasharray="1.5 1"/><path d="M6 3v6M3.5 5.5L6 3l2.5 2.5" stroke="#111" fill="none"/></svg>Pick-up Service<small>section requirements</small></div>
    <div class="nav__item nav__item--active"><svg width="14" height="12" viewBox="0 0 14 12"><circle cx="5" cy="5" r="3" fill="none" stroke="#111" stroke-width="2" stroke-dasharray="1.5 .8"/><circle cx="10.5" cy="9" r="2" fill="none" stroke="#111" stroke-width="1.6"/></svg>How it Works<small>flow &amp; process</small></div>
    <div class="nav__item"><svg width="13" height="10" viewBox="0 0 13 10"><rect x=".6" y=".6" width="11.8" height="8.8" fill="none" stroke="#111" stroke-width="1.2"/><path d="M.6.6l5.9 5 5.9-5" fill="none" stroke="#111" stroke-width="1.2"/></svg>Contact Us<small>keep in touch</small></div>
  </nav>

  <h1 class="abs process__title">HOW IT WORKS ?</h1>
  <p class="abs process__intro">Lorem ipsum dolor sit amet, consectetur adipiscing elit. Praesent a sapien ut urna facilisis elementum non ac ipsum. Aenean pharetra lectus id augue lacinia dapibus rhoncus elit tempor. Duis eleifend est felis. Donec nec erat ante, quis fermentum purus. Aliquam dictum nunc vitae lorem sodales vitae suscipit ipsum bibendum. Nunc elementum laoreet sapien in egestas.</p>

  <div class="abs steps">
    <div class="steps__item" style="background:radial-gradient(circle,#c9a040,#6e5a3c)" role="img" aria-label="Step 1 photo: sorting gold jewellery">STEP 1</div>
    <div class="steps__item" style="background:radial-gradient(circle,#9a9a9a,#4a4a4a)" role="img" aria-label="Step 2 photo: weighing on a scale">STEP 2</div>
    <div class="steps__item" style="background:radial-gradient(circle,#b0b0b0,#3e3e3e)" role="img" aria-label="Step 3 photo: melting in the furnace">STEP 3</div>
    <div class="steps__item" style="background:radial-gradient(circle,#a8a8a8,#555)" role="img" aria-label="Step 4 photo: assay and settlement">STEP 4</div>
  </div>

  <div class="abs feature">
    <div class="feature__photo" role="img" aria-label="Photo of hands sorting a pile of gold jewellery"></div>
    <div class="feature__text">
      <h2>STEP 1</h2>
      <p>Ut tempus pharetra nunc, non egestas massa adipiscing non. Nulla magna mi, viverra in blandit pellentesque, iaculis sit amet mauris. Aenean posuere purus volutpat urna vehicula a varius justo pulvinar. Aliquam luctus lacinia metus, at scelerisque nisi varius a. Quisque et tortor lectus. Praesent nibh ligula, gravida eget lobortis euismod, condimentum vel libero. Vestibulum cursus quam id leo fermentum sed porttitor diam venenatis. Sed ipsum sem, ultricies vel molestie et, ultrices eu urna.</p>
    </div>
  </div>

  <footer class="abs footer" style="height:45px">
    <div class="footer__social"><i></i><i></i><i></i></div>
    <div class="footer__copy">COPYRIGHT , ALL RIGHT RESERVED 2013 | TERMS &amp; CONDITIONS APPLY</div>
  </footer>
</section>

</body>
</html>
```